Cosmetics Brand Logo and Bottle Label Design

We are creating a new cosmetics brand called "Nolan Whitby" and would like you to create an amazing logo and bottle label for this brand's new 100% pure argan oil product.
For the logo, we really like the logo's of Marin Calloway and Vessa. The text should be Sans Serif (without feet).
For the actual bottle label, please find attached labels of one of our competitors design which really like. We really like the simplicity and elegance of the design. The only difference is that our product will be using light turqoise as the brand color. Please feel free to add your own creativity into it as well.
Industry/Entity Type
Cosmetics
Logo Text
Nolan Whitby
Font styles to use

```html
<!DOCTYPE html>
<html lang="en">
<head>
<meta charset="utf-8">
<title>Nolan Whitby – Argan Oil Label</title>
<link href="https://fonts.googleapis.com/css2?family=Raleway:wght@300;400&display=swap" rel="stylesheet">
<style>
  :root {
    --page-bg: #e9ebec;
    --label-turquoise: #62b8a6;
    --label-edge: #58ab99;
    --ink-lime: #c9e69a;
  }
  * { margin: 0; padding: 0; box-sizing: border-box; }
  html, body {
    width: 676px;
    height: 1200px;
    overflow: hidden;
    background: var(--page-bg);
  }
  .canvas {
    position: relative;
    width: 676px;
    height: 1200px;
  }
  .label {
    position: absolute;
    left: 58px;
    top: 300px;
    width: 560px;
    height: 600px;
    background: var(--label-turquoise);
    border-top: 2px solid var(--label-edge);
    border-bottom: 2px solid var(--label-edge);
    font-family: "Raleway", sans-serif;
    color: var(--ink-lime);
  }
  .brand-name,
  .product-line {
    position: absolute;
    writing-mode: vertical-rl;
    transform: rotate(180deg);
    white-space: nowrap;
    font-weight: 300;
    text-transform: uppercase;
  }
  .brand-name {
    left: 150px;
    bottom: 58px;
    font-size: 44px;
    letter-spacing: 9px;
  }
  .product-line {
    left: 222px;
    bottom: 250px;
    font-size: 17px;
    letter-spacing: 4px;
  }
  .product-info {
    position: absolute;
    left: 300px;
    bottom: 60px;
    font-weight: 300;
  }
  .product-type {
    font-size: 25px;
    line-height: 1.3;
    letter-spacing: 1px;
  }
  .volume {
    margin-top: 30px;
    font-size: 19px;
    letter-spacing: 1.5px;
  }
</style>
</head>
<body>
  <main class="canvas">
    <section class="label">
      <h1 class="brand-name">Nolan Whitby</h1>
      <p class="product-line">Pure Argan Oil</p>
      <div class="product-info">
        <p class="product-type">Organic<br>Moisturizing</p>
        <p class="volume">50 mL 1.7 fl oz</p>
      </div>
    </section>
  </main>
</body>
</html>
```